Business Card Design needed for start up company Pramora

In need of a new business card designed for a start up company based in Sydney, Pramora is a new start up innovative Company, our mission it to make property accessible for everyday Australian and to become the leading Real Estate platform in Australia. We want it to be fresh and clean.

Industry/Entity Type

Financial

Contact Information for Business Card

Section for Name
Section for Title

PRAMORA - Where Doors Open Wide
Mobile:
Direct:

Font styles to use
Sans Serif

Colors
33a6d7
0692cd
0255a3
ffffff

Requirements
Must have
• Logo, all business card details

```html
<!DOCTYPE html>
<html lang="en">
<head>
<meta charset="UTF-8">
<title>Pramora – Business Card</title>
<link href="https://fonts.googleapis.com/css2?family=Roboto:wght@300;400;500;900&display=swap" rel="stylesheet">
<style>
  :root {
    --sky: #33a6d7;
    --azure: #0692cd;
    --navy: #0255a3;
    --deep-navy: #1f4a7e;
    --band-navy: #1e4b85;
    --white: #ffffff;
    --ink: #1b2a3a;
    --stage: #e6e9ec;
  }
  * { margin: 0; padding: 0; box-sizing: border-box; }
  html, body {
    width: 1200px; height: 900px; overflow: hidden;
    background: var(--stage);
    font-family: "Roboto", Arial, sans-serif;
  }
  .sheet {
    position: relative; width: 1200px; height: 900px;
    display: flex; flex-direction: column; align-items: center; justify-content: center; gap: 60px;
  }
  .card {
    position: relative; width: 560px; height: 320px;
    border-radius: 18px; overflow: hidden;
    box-shadow: 0 10px 24px rgba(20, 35, 55, 0.22);
  }

  /* Back side */
  .card--back { background: var(--deep-navy); display: flex; align-items: center; justify-content: center; }
  .brand { display: flex; align-items: center; gap: 14px; }
  .brand__dot { border-radius: 50%; background: var(--sky); flex: none; }
  .brand__name { font-weight: 900; letter-spacing: 1px; line-height: 1; }
  .card--back .brand__dot { width: 62px; height: 62px; }
  .card--back .brand__name { color: var(--white); font-size: 68px; }

  /* Front side */
  .card--front { background: var(--white); }
  .card__art { position: absolute; inset: 0; }
  .card--front .brand { position: absolute; left: 34px; top: 30px; gap: 10px; }
  .card--front .brand__dot { width: 34px; height: 34px; }
  .card--front .brand__name { color: var(--band-navy); font-size: 38px; }

  .contacts { position: absolute; left: 34px; top: 110px; list-style: none; }
  .contacts li { display: flex; align-items: center; gap: 10px; height: 26px; font-size: 14px; color: var(--ink); }
  .contacts .icon {
    width: 18px; height: 18px; border-radius: 3px; background: var(--band-navy);
    display: flex; align-items: center; justify-content: center; flex: none;
  }
  .contacts svg { width: 12px; height: 12px; }

  .holder { position: absolute; left: 352px; top: 74px; color: var(--white); text-align: center; width: 190px; }
  .holder__name { font-size: 22px; font-weight: 400; letter-spacing: 1.5px; }
  .holder__title { font-size: 11px; font-weight: 300; letter-spacing: 1px; margin-top: 2px; }

  .address { position: absolute; left: 300px; top: 236px; color: var(--white); font-size: 14px; line-height: 1.45; font-weight: 400; }
</style>
</head>
<body>
<main class="sheet">

  <section class="card card--front" aria-label="Business card front">
    <svg class="card__art" viewBox="0 0 560 320" aria-hidden="true">
      <polygon points="400,0 560,0 560,320 190,320" fill="#2a9bd6"/>
      <polygon points="318,70 340,54 560,54 560,140 318,140" fill="var(--band-navy)"/>
      <polygon points="318,70 340,54 340,70" fill="#173d6c"/>
    </svg>

    <div class="brand">
      <span class="brand__dot"></span>
      <span class="brand__name">PRAMORA</span>
    </div>

    <ul class="contacts">
      <li><span class="icon"><svg viewBox="0 0 12 12"><path d="M3 1l2 2-1 1.3c.6 1.3 1.4 2.1 2.7 2.7L8 6l2 2-1.2 1.8C5 9.5 2.5 7 2.2 3.2z" fill="#fff"/></svg></span>02 8000 4172</li>
      <li><span class="icon"><svg viewBox="0 0 12 12"><rect x="3.5" y="1" width="5" height="10" rx="1" fill="none" stroke="#fff" stroke-width="1.2"/><circle cx="6" cy="9.3" r=".6" fill="#fff"/></svg></span>0400 118 265</li>
      <li><span class="icon"><svg viewBox="0 0 12 12"><rect x="1.5" y="3" width="9" height="6.5" fill="none" stroke="#fff" stroke-width="1.1"/><path d="M1.5 3L6 6.8 10.5 3" fill="none" stroke="#fff" stroke-width="1.1"/></svg></span>liam@pramora.au</li>
      <li><span class="icon"><svg viewBox="0 0 12 12"><circle cx="6" cy="6" r="4.5" fill="none" stroke="#fff" stroke-width="1.1"/><path d="M1.5 6h9M6 1.5c-2 2.5-2 6.5 0 9M6 1.5c2 2.5 2 6.5 0 9" fill="none" stroke="#fff" stroke-width=".9"/></svg></span>www.pramora.au</li>
    </ul>

    <div class="holder">
      <p class="holder__name">LIAM CARTER</p>
      <p class="holder__title">OWNER</p>
    </div>

    <p class="address">48 Harbour Lane, Level 7<br>Sydney NSW 2000</p>
  </section>

  <section class="card card--back" aria-label="Business card back">
    <div class="brand">
      <span class="brand__dot"></span>
      <span class="brand__name">PRAMORA</span>
    </div>
  </section>

</main>
</body>
</html>
```